Velqora new official website

We need a new design for our website www.velqora-example.com We are web marketing publishers and our website must be attractive for clients. That's why we need to "refresh" it. The main colour of our logo is orange, and this is an indication for the colours of the website too. We need the design for the homepage and the design of inner pages. Here is the list of the various sections of the website:
- ABOUT US: Who we are/Certificates/Offices/Team
- SERVICES: SEM/Display/Email Marketing and coregistration/ad networking
- PROJECTS/NETWORK/BRANDS: We need one page per country with screenshots of the websites and very short descriptions.
- VELQORA & CHARITY
- WORK WITH US
- CONTACT US
- NEWS

```html
<!DOCTYPE html>
<html lang="en">
<head>
<meta charset="utf-8">
<title>Velqora – Home</title>
<link rel="stylesheet" href="https://fonts.googleapis.com/css2?family=Arimo:wght@400;700&family=Roboto+Condensed:wght@700&display=swap">
<style>
:root{
  --orange:#f7860f;
  --orange-deep:#ee7400;
  --orange-light:#fb9a2c;
  --grey-text:#555;
  --grey-dark:#333;
  --grey-tab:#c9c9c9;
  --panel:#f1f1f1;
  --white:#fff;
  --line:#e2e2e2;
}
*{margin:0;padding:0;box-sizing:border-box}
html,body{width:939px;height:1200px;overflow:hidden}
body{position:relative;font-family:Arimo,Arial,sans-serif;color:var(--grey-text);
  background:linear-gradient(to bottom,var(--orange-light) 130px,var(--orange) 500px,var(--orange-deep) 1127px);}
.abs{position:absolute}

/* header */
.site-header{position:absolute;left:0;top:0;width:939px;height:130px;
  background:linear-gradient(#fff,#f3f3f3);border-bottom:3px solid var(--orange-deep)}
.brand{position:absolute;left:97px;top:34px;display:flex;align-items:center;gap:8px}
.brand-name{font:700 46px Arimo,Arial,sans-serif;color:var(--orange-deep);letter-spacing:-1px}
.brand-dot{width:30px;height:30px;border-radius:50%;background:var(--orange-deep)}
.main-nav{position:absolute;left:294px;top:103px;display:flex;gap:6px}
.main-nav a{display:block;height:27px;line-height:28px;padding:0 9px;border-radius:13px 13px 0 0;white-space:nowrap;
  background:var(--orange);color:#fff;font-size:12.5px;text-decoration:none}
.main-nav a.active{background:var(--grey-tab);color:var(--grey-dark)}

/* hero */
.hero-title{position:absolute;left:170px;top:178px;width:236px;text-align:center;color:#fff;
  font-family:"Roboto Condensed",Arial,sans-serif;font-weight:700;line-height:1.05}
.hero-title .l1,.hero-title .l2{display:block;font-size:37px}
.hero-title .l3{display:block;font-size:62px;margin-top:-2px}
.hero-photo{left:423px;top:141px;width:330px;height:213px;
  background:linear-gradient(to bottom,#f6a547,#e9e9ee 60%,#cfd6df);border-radius:4px 4px 0 0}

/* content panel */
.panel{left:99px;top:355px;width:732px;height:723px;background:var(--panel);border-radius:12px;
  box-shadow:0 3px 8px rgba(0,0,0,.25)}

/* left boxes */
.side-box{position:absolute;left:117px;width:221px;background:#fff;border:1px solid var(--line);padding:56px 12px 8px}
.side-box h2{position:absolute;left:-8px;right:-8px;top:11px;height:35px;line-height:37px;padding-left:20px;white-space:nowrap;
  background:linear-gradient(var(--orange-light),var(--orange-deep));color:#fff;font-weight:400;font-size:12.5px;
  box-shadow:0 2px 3px rgba(0,0,0,.2)}
.side-box h2::before,.side-box h2::after{content:"";position:absolute;top:-7px;border-bottom:7px solid #b85700}
.side-box h2::before{left:0;border-left:8px solid transparent}
.side-box h2::after{right:0;border-right:8px solid transparent}
.side-box p{font-size:9.6px;line-height:14px;text-align:justify}
.more{color:var(--orange-deep);font-size:9.6px;text-decoration:none;white-space:nowrap}
.side-box .more{display:block;text-align:right;margin:4px 6px 0 0}
.offices{font-size:9px;line-height:13px;padding-top:2px}
.offices dt{color:var(--orange-deep);display:inline}
.offices dt.head{font-weight:700}
.offices dd{display:inline}
.offices div{margin-bottom:5px;color:#444}

/* expertise */
.expertise-banner{left:358px;top:366px;width:466px;height:49px;
  background:linear-gradient(90deg,#dcdcdc,#f4f4f4 40%,#c8c8c8)}
.expertise-banner span{position:absolute;right:10px;top:18px;font-size:16px;color:#444;letter-spacing:.5px}
.expertise-banner b{color:var(--orange-deep)}
.fields{left:358px;top:423px;width:466px;height:280px;background:#fff;border-radius:3px}
.field{position:absolute;left:25px;right:30px}
.field h3{color:var(--orange-deep);font-size:14px;font-weight:700;margin-bottom:8px;white-space:nowrap}
.field p{font-size:9.1px;line-height:13px;color:#555}
.field .more{position:absolute;right:0;font-size:9.2px}

/* news */
.news-tab{position:absolute;height:30px;line-height:30px;padding:0 15px;background:var(--orange);color:#fff;white-space:nowrap;
  font-weight:700;font-size:13.5px;border-radius:14px 14px 0 0}
.news-photo{left:363px;top:755px;width:214px;height:129px;background:linear-gradient(#7b8794,#3e3a38 70%,#2b2b2b)}
.news-caption{left:363px;top:884px;width:214px;height:32px;background:var(--orange);color:#fff;
  font-size:8.1px;line-height:12px;padding:3px 5px}
.adtech{left:587px;top:750px;width:231px;height:168px;border:2px solid var(--orange);background:#fff;padding:10px 9px}
.adtech li{list-style:none;font-size:7.9px;line-height:11.6px;margin-bottom:7px}
.adtech .t{color:#555;display:block;margin-bottom:2px}
.adtech .x{color:var(--orange-deep)}

/* search & partners */
.search{left:616px;top:953px;width:201px;height:20px;display:flex}
.search .field-in{flex:1;background:#fff;border:1px solid #ddd;border-radius:2px 0 0 2px}
.search button{width:47px;background:#555;color:#fff;border:0;font:10px Arimo,Arial,sans-serif}
.badge{position:absolute;top:1002px;height:52px;border-radius:3px}
.social{position:absolute;top:1021px;width:33px;height:33px;border-radius:5px}

/* footer */
.site-footer{position:absolute;left:0;top:1127px;width:939px;height:73px;background:linear-gradient(#fff,#ededed);
  text-align:center;font-size:10.5px;color:#444}
.site-footer .addr{position:absolute;top:15px;width:100%}
.site-footer .copy{position:absolute;top:50px;width:100%;font-size:10px}
</style>
</head>
<body>

<header class="site-header">
  <div class="brand"><span class="brand-name">velqora</span><span class="brand-dot"></span></div>
  <nav class="main-nav">
    <a class="active" href="#">About Us</a><a href="#">Services</a><a href="#">Projects</a>
    <a href="#">Velqora&amp; Charity</a><a href="#">Work with us</a><a href="#">Contact Us</a><a href="#">News</a>
  </nav>
</header>

<h1 class="hero-title"><span class="l1">The Main Way</span><span class="l2">To Your</span><span class="l3">Business</span></h1>
<div class="abs hero-photo" role="img" aria-label="Photo of two businessmen in shirts and ties beside a flip chart with a rising line graph"></div>

<div class="abs panel"></div>

<section class="side-box" style="top:366px">
  <h2>Scope &amp; Mission</h2>
  <p>Our aim is creating adding value on our customers sales through technology and web marketing by means of the most modern web advertising systems. We help our customers in developing new sales stretegies based on the web marketing. We watch the market and support our customers in achieving excellent visibility on the newest advertising channels. We are able to offer a wide range of either standard or tailored solutions.</p>
  <a class="more" href="#">see more</a>
</section>

<section class="side-box" style="top:599px">
  <h2>Clients strategies and web know how</h2>
  <p>We cooperate with the MAIN international brands in the fields of tourism, finance, fashion, durable goods, technologies &amp; communication. We help our customers in finding the way to succeed on every single one of their campaigns and on the brand awareness. We implement our strategies also in cooperation with some well known international partners who cooperate with us in tracing and checking statistics and performances.</p>
  <a class="more" href="#">see more</a>
</section>

<section class="side-box" style="top:844px">
  <h2>Our Offices</h2>
  <dl class="offices">
    <div><dt class="head">HEAD OFFICE:</dt> <dd>Velqora srl - Via Lorenzi 14<br>65100 Castelmare (PE) - ITALY<br>Tel.+39 085000149 Fax +39 (0)2 70000796</dd></div>
    <div><dt>BRANCH OFFICE:</dt> <dd>C-22 Nalanda, Techhub<br>695000 Varunapuram - INDIA</dd></div>
    <div><dt>BRANCH OFFICE:</dt> <dd>Meridian House,<br>Lotus Road<br>tel 0110 000 0628 New Delhi - INDIA</dd></div>
    <div><dt>BRANCH OFFICE:</dt> <dd>Carrer de Solana 12, 2-1<br>08000 Barcelona - España</dd></div>
  </dl>
</section>

<div class="abs expertise-banner" role="img" aria-label="Banner with a businessman image fading into the word expertise">
  <span>FIELDS OF <b>EXPERTISE</b></span>
</div>

<section class="abs fields">
  <div class="field" style="top:8px"><h3>Tourism</h3><p>Tourism has been our first passion.Today it is our MAIN business and generates our MAIN income.</p><a class="more" style="top:44px" href="#">see more</a></div>
  <div class="field" style="top:57px"><h3>Finance</h3><p>VELQORA has been working for a long time with the MAIN brands in the international world of finance.</p><a class="more" style="top:46px" href="#">see more</a></div>
  <div class="field" style="top:106px"><h3>Technologies &amp; Communications</h3><p>Dsl, lap tops, hardware, isn't that a hard job to keep updated about it?</p><a class="more" style="top:35px" href="#">see more</a></div>
  <div class="field" style="top:153px"><h3>Durable Goods</h3><p>As publisher we help the MAIN brands in the field of automotive, appliances, business equipment, electronic equipment, electronic equipment</p><a class="more" style="top:47px" href="#">see more</a></div>
  <div class="field" style="top:212px"><h3>Fashion</h3><p>The new frontier for our company is the world of fashion; We believe that today, television and the Internet are merging, at least when it comes to advertising and reaching potential customers.</p><a class="more" style="top:55px" href="#">see more</a></div>
</section>

<div class="news-tab" style="left:363px;top:725px">Velqora News</div>
<div class="abs news-photo" role="img" aria-label="Photo of three smiling colleagues at an industry trade event"></div>
<div class="abs news-caption">Parallel to Northcast event, Linkora invited international top publisher... [read more]</div>

<div class="news-tab" style="left:587px;top:725px">Adtech News</div>
<ul class="abs adtech">
  <li><span class="t">Searchly Goes Big For Browsa TV Ad</span><span class="x">During the season finale of 'Late Weekend Live' Searchly premiered its new ad for Browsa and its other services - heavily ...</span></li>
  <li><span class="t">80 Percent of U.S. Users Viewed Online Video in April</span><span class="x">Video ads reached 42 percent of users over the course of the month.</span></li>
  <li><span class="t">18% U.S. Smartphone Users Access Location-Based Services</span><span class="x">Thirteen- to 34-year-olds account for over two-thirds of users.</span></li>
</ul>

<form class="abs search"><span class="field-in"></span><button type="button">Search</button></form>

<div class="badge" style="left:365px;width:50px;background:var(--orange)"></div>
<div class="badge" style="left:430px;width:84px;background:#d9d9d9"></div>
<div class="badge" style="left:518px;width:150px;background:#e6e6e6"></div>
<div class="social" style="left:697px;background:#3a5a98"></div>
<div class="social" style="left:741px;background:#2a7ab0"></div>
<div class="social" style="left:783px;background:#3fa9e0"></div>

<footer class="site-footer">
  <p class="addr">VELQORA, Via Lorenzi,14 - I-65100 Castelmare (PE) Italy &nbsp; Tel.++39 085000149 Fax ++39 (0)2 70000796 ,VAT IT 01800000000</p>
  <p class="copy">© Designed and developed by Velqora. 2009</p>
</footer>

</body>
</html>
```